Ha4Giggle website

We need a website called Ha 4 Giggle (ha4giggle.com).
This site is for fun (just like 7lol.com, flopdiary.com, chucklepapa.com etc. You know what I mean, right?)
so we are open to different designs/looks. We are looking for a simple and clean and fun design to make it easy to use for our users.

The design of Ha4Giggle should be different from other fun site (better than others, I mean), and this is what we want you to do.

The style for our site should be in (or be similar to, at least) the BLOG way, (If you can't catch my words, have a look at 7LOL or Flopdiary).

But at meantime, I'd like to stress again that we want this site be different from the sites like 7LOL and FlopDiary.
Updates

i have a logo for the website now.

http://images.artmarketo.com/designs/56722_788142_42200_thumbnail.jpg

pls try to fit this logo into the website design.

Requirements
Must have
• We need at least following pages designed:

1. front page (index.jpg)

2. login form page (login.jpg)

3. registeration form page (register.jpg)

4. content page (post.jpg)

5. submit photo form page (submit.jpg)

6. user profile page (user_center.jpg)

```html
<!DOCTYPE html>
<html lang="en">
<head>
<meta charset="utf-8">
<title>Ha4Giggle – Submit</title>
<link rel="stylesheet" href="https://fonts.googleapis.com/css2?family=Arimo:wght@400;700&family=Lobster&display=swap">
<style>
:root{
  --page-bg:#e2e1db;
  --panel:#ffffff;
  --field:#b3b3b3;
  --ink:#222222;
  --ink-soft:#444444;
  --heading:#1f3a45;
  --red:#b41212;
  --red-band:#d01210;
  --red-deep:#a10202;
  --red-tab:#a60d0d;
  --link:#3b5998;
  --blue-btn:#1a8fc4;
  --box-bg:#ededed;
  --title-pink:#f5c9c2;
}
*{box-sizing:border-box;margin:0;padding:0}
html,body{width:1200px;height:900px;overflow:hidden}
body{position:relative;background:var(--page-bg);font-family:"Arimo",Arial,sans-serif;color:var(--ink)}
.abs{position:absolute}

/* sidebar social box */
.social-box{left:113px;top:-4px;width:233px;height:202px;border:2px dotted #333;padding:2px}
.social-box .inner{width:100%;height:100%;background:var(--box-bg);border:1px solid #bbb}
.like-btn{left:131px;top:6px;width:46px;height:20px;border:1px solid #c8c8d8;border-radius:3px;background:#f3f4f8;font-size:11px;color:#3b5998;text-align:center;line-height:18px;font-weight:700}
.like-text{left:200px;top:5px;width:120px;font-size:11px;line-height:14px;color:#555}
.like-text b{font-weight:400;color:var(--link)}
.fan{top:49px;width:28px;height:28px;background:linear-gradient(#8a7a6a,#c9b8a4)}
.rule{left:131px;width:185px;border-top:1px dashed #999}
.follow-btn{left:162px;top:98px;width:130px;height:20px;border:1px solid #ccc;border-radius:3px;background:linear-gradient(#fff,#e6e6e6);font-size:11px;font-weight:700;text-align:center;line-height:18px}
.followers{left:192px;top:123px;width:80px;height:18px;border:1px solid #bbb;background:#fff;border-radius:2px;font-size:10px;text-align:center;line-height:16px;color:#333}
.plus-btn{left:131px;top:152px;width:29px;height:18px;border:1px solid #ccc;border-radius:2px;background:#f5f5f5;font-size:10px;font-weight:700;color:#c33;text-align:center;line-height:16px}
.plus-count{left:164px;top:152px;width:31px;height:18px;border:1px solid #ccc;background:#fff;font-size:10px;color:#666;text-align:center;line-height:16px}
.recommend{left:209px;top:155px;font-size:10px;color:#555}

/* latest comments */
.side-title{left:110px;top:210px;width:224px;text-align:center;font-family:"Lobster",cursive;font-size:25px;color:#333}
.comment{left:110px;width:236px;border:3px dotted #333;padding:2px}
.comment .card{position:relative;width:100%;height:100%;background:#fff;border:1px solid #ccc}
.avatar{position:absolute;left:10px;top:12px;width:41px;height:41px}
.quote{position:absolute;left:61px;top:8px;width:165px;font-size:13px;line-height:15.5px;color:#111}
.user{position:absolute;left:61px;font-family:"Lobster",cursive;font-size:12px;color:#7a0000}

/* main form panel */
.panel{left:366px;top:0;width:722px;height:678px;background:var(--panel)}
.label{left:462px;font-size:13px;color:var(--ink)}
.label em{font-style:italic}
.field{left:462px;width:274px;height:26px;background:var(--field)}
.step{left:378px;width:68px;height:68px}
.anon-box{left:462px;top:198px;width:11px;height:11px;background:#555}
.anon{left:481px;top:197px;font-size:12px;color:#c40000}
.profit{left:458px;top:528px;font-family:"Lobster",cursive;font-size:38px;color:var(--heading)}
.submit-btn{left:463px;top:600px;width:90px;height:45px;background:var(--blue-btn);color:#fff;font-size:14px;text-align:center;line-height:45px}

/* footer */
.band{left:0;top:719px;width:1200px;height:72px;background:var(--red-band)}
.band-rule{left:0;top:790px;width:1200px;border-top:1px dashed #f06060}
.footer-base{left:0;top:791px;width:1200px;height:109px;background:var(--red-deep)}
.tabs{left:360px;top:700px}
.tab-text{top:729px;font-size:13px;color:#fff}
.brand{left:170px;top:770px;display:flex;align-items:center;gap:7px;font-size:17px;font-weight:700;color:#fff}
.brand i{display:block;width:14px;height:14px;border-radius:50%;background:#fff}
.footer-title{left:370px;top:800px;font-family:"Lobster",cursive;font-size:29px;color:var(--title-pink)}
.footer-text{left:370px;top:849px;width:660px;font-size:12px;line-height:15px;color:#fff}
</style>
</head>
<body>

<!-- sidebar social box -->
<div class="abs social-box"><div class="inner"></div></div>
<div class="abs like-btn">Like</div>
<p class="abs like-text"><b>Marco Bellini</b>, <b>Rossetti</b> and 3,220 others like this.</p>
<div class="abs fan" style="left:131px" role="img" aria-label="Fan profile photo"></div>
<div class="abs fan" style="left:162px" role="img" aria-label="Fan profile photo"></div>
<div class="abs fan" style="left:193px" role="img" aria-label="Fan profile photo"></div>
<div class="abs fan" style="left:224px" role="img" aria-label="Fan profile photo"></div>
<div class="abs rule" style="top:90px"></div>
<div class="abs follow-btn">Follow @ha4giggle</div>
<div class="abs followers">677K followers</div>
<div class="abs rule" style="top:147px"></div>
<div class="abs plus-btn">+1</div>
<div class="abs plus-count">63k</div>
<p class="abs recommend">Recommend on Searchly</p>

<!-- latest comments -->
<h2 class="abs side-title">Latest comments</h2>
<div class="abs comment" style="top:253px;height:95px"><div class="card">
  <div class="avatar" role="img" aria-label="User avatar" style="background:linear-gradient(#3c9ac8,#2c7fae)"></div>
  <p class="quote">“Lorem ipsum dolor sit amet, consectetur adipisc-ing eli. Praesent posuere...”</p>
  <p class="user" style="top:64px">Username</p>
</div></div>
<div class="abs comment" style="top:364px;height:96px"><div class="card">
  <div class="avatar" role="img" aria-label="User avatar" style="background:linear-gradient(#e8e8e8,#bcbcbc)"></div>
  <p class="quote">“Lorem ipsum dolor sit amet, consectetur adipisc-ing eli. Praesent posuere...”</p>
  <p class="user" style="top:60px">Username</p>
</div></div>
<div class="abs comment" style="top:471px;height:96px"><div class="card">
  <div class="avatar" role="img" aria-label="User avatar" style="background:linear-gradient(#9a9a9a,#333)"></div>
  <p class="quote">“Lorem ipsum dolor sit amet, consectetur adipisc-ing eli. Praesent posuere...”</p>
  <p class="user" style="top:60px">Username</p>
</div></div>

<!-- submit form -->
<main class="abs panel"></main>
<div class="abs field" style="top:1px"></div>
<p class="abs label" style="top:41px"><em>or</em> give us a link of a <b>video</b></p>
<div class="abs field" style="top:62px"></div>

<svg class="abs step" style="top:131px" viewBox="0 0 68 68" aria-hidden="true">
  <circle cx="34" cy="34" r="32" fill="#fff" stroke="#b41212" stroke-width="1.5" stroke-dasharray="2 2"/>
  <circle cx="34" cy="34" r="29" fill="#b41212"/>
  <circle cx="34" cy="34" r="26.5" fill="none" stroke="#fff" stroke-width="1" stroke-dasharray="1.5 2"/>
  <text x="34" y="46" text-anchor="middle" font-family="Lobster, cursive" font-size="34" fill="#fff">2</text>
</svg>
<p class="abs label" style="top:142px">your name</p>
<div class="abs field" style="top:162px"></div>
<div class="abs anon-box"></div>
<p class="abs anon">I want to submit as anonymous</p>
<p class="abs label" style="top:239px">your eMail (never displayed)</p>
<div class="abs field" style="top:260px"></div>

<svg class="abs step" style="top:308px" viewBox="0 0 68 68" aria-hidden="true">
  <circle cx="34" cy="34" r="32" fill="#fff" stroke="#b41212" stroke-width="1.5" stroke-dasharray="2 2"/>
  <circle cx="34" cy="34" r="29" fill="#b41212"/>
  <circle cx="34" cy="34" r="26.5" fill="none" stroke="#fff" stroke-width="1" stroke-dasharray="1.5 2"/>
  <text x="34" y="46" text-anchor="middle" font-family="Lobster, cursive" font-size="34" fill="#fff">3</text>
</svg>
<p class="abs label" style="top:317px">add a title to your submition</p>
<div class="abs field" style="top:338px"></div>
<p class="abs label" style="top:380px">add a description of your image</p>
<div class="abs field" style="top:401px"></div>
<p class="abs label" style="top:444px">add a source (from where you got this image)</p>
<div class="abs field" style="top:465px"></div>

<svg class="abs step" style="top:518px" viewBox="0 0 68 68" aria-hidden="true">
  <circle cx="34" cy="34" r="32" fill="#fff" stroke="#b41212" stroke-width="1.5" stroke-dasharray="2 2"/>
  <circle cx="34" cy="34" r="29" fill="#b41212"/>
  <circle cx="34" cy="34" r="26.5" fill="none" stroke="#fff" stroke-width="1" stroke-dasharray="1.5 2"/>
  <text x="34" y="46" text-anchor="middle" font-family="Lobster, cursive" font-size="34" fill="#fff">4</text>
</svg>
<h2 class="abs profit">Profit!!!</h2>
<div class="abs submit-btn">Submit it!</div>

<!-- footer -->
<div class="abs band"></div>
<div class="abs band-rule"></div>
<div class="abs footer-base"></div>
<svg class="abs tabs" width="400" height="70" viewBox="360 700 400 70" aria-hidden="true">
  <polygon points="370,704 493,713 486,760 368,760" fill="#a60d0d"/>
  <polygon points="500,716 601,706 594,760 498,760" fill="#a60d0d"/>
  <polygon points="617,704 746,716 746,760 614,760" fill="#a60d0d"/>
</svg>
<a class="abs tab-text" style="left:378px">About ha4giggle</a>
<a class="abs tab-text" style="left:520px;top:731px">Contact Us</a>
<a class="abs tab-text" style="left:627px">Legal information</a>

<div class="abs brand"><i></i>Ha4Giggle</div>
<h2 class="abs footer-title">ha4giggle</h2>
<p class="abs footer-text">Lorem ipsum dolor sit amet, consectetur adipiscing elit. Praesent posuere faucibus tempus. Duis non diam risus. Aliquam venenatis commodo quam vitae congue. Sed nec dui nibh, vitae dapibus diam.</p>

</body>
</html>
```